Verpackung für Online-Verkauf von Produkten für Eltern
Zielgruppe
Online-Verkauf von Produkten für Eltern (Kinderprodukte und nützliche Produkte für Zuhause)
Aufgabenstellung
Verpackung soll eher schlicht sein, nicht zu viele Farben und nicht verspielt. Klare Strukturen, aber trotzdem vertrauenserweckend und sanft. Es sollen keine zusätzlichen Bilder (z.B. von Eltern oder Kindern) eingefügt werden. Bitte die in der Anleitung erwähnten Symbole aus Stockmaterial ziehen.
Die benutzen Farben und Schriftart soll zum Logo passen (hier wurde verwendet: Quicksand 229, Grau #38444d, Gelb-grün #949260).
Knifelines anbei, auch die Inhalte/ Texte sowie das Logo werden übermittelt.
Die genaue Anleitung ist der Datei zu entnehmen (inklusive der Ausrichtung der Texte).

```html
<!DOCTYPE html>
<html lang="de">
<head>
<meta charset="utf-8">
<title>Nestora – Faltschachtel Kindersicherung</title>
<link rel="stylesheet" href="https://fonts.googleapis.com/css2?family=Quicksand:wght@400;500;600;700&display=swap">
<style>
  :root {
    --board: #323f4b;
    --ink-white: #ffffff;
    --ink-muted: #a6afb7;
    --ink-olive: #949260;
    --die-cut: #d9782b;
    --fold: #4f9aa6;
    --panel-edge: #49586a;
    --measure: #2c7fc4;
  }
  * { margin: 0; padding: 0; box-sizing: border-box; }
  html, body { width: 1200px; height: 1109px; overflow: hidden; background: var(--board); }
  body { font-family: "Quicksand", sans-serif; color: var(--ink-white); }
  .dieline-sheet { position: relative; width: 1200px; height: 1109px; }
  .dieline-sheet > svg.lines { position: absolute; inset: 0; }
  .abs { position: absolute; }
  .center-x { left: 297px; width: 605px; text-align: center; }

  .thanks { top: 55px; font-size: 16px; color: var(--ink-olive); font-weight: 500; }

  .features { top: 194px; font-size: 14px; line-height: 24.4px; letter-spacing: .1px; }
  .features li { list-style: none; display: flex; align-items: center; gap: 6px; }
  .features svg { width: 13px; height: 13px; flex: none; }
  .features--de { left: 330px; color: var(--ink-white); }
  .features--en { left: 636px; color: var(--ink-muted); }

  .warning { top: 337px; font-size: 7.6px; line-height: 8.4px; }
  .warning p + p { margin-top: 8px; }
  .warning--de { left: 334px; color: var(--ink-white); }
  .warning--en { left: 645px; color: #6f7c88; }

  .imprint { top: 144px; left: 183px; height: 300px; writing-mode: vertical-rl;
    font-size: 7.6px; line-height: 10.3px; color: var(--ink-white); }
  .imprint .gap { margin-left: 9px; }

  .wordmark { font-weight: 500; color: var(--ink-white); letter-spacing: 1px; line-height: 1; }
  .wordmark--lid { top: 492px; font-size: 44px; }
  .wordmark--front { top: 650px; font-size: 82px; }
  .wordmark--base { top: 961px; font-size: 44px; }
  .tagline { font-size: 17px; color: var(--ink-olive); font-weight: 500; }
  .tagline--lid { top: 535px; }
  .tagline--front { top: 725px; }
  .tagline--base { top: 1016px; font-size: 16.5px; }

  .help-sticker { left: 782px; top: 473px; width: 90px; height: 90px; border-radius: 50%;
    background: var(--ink-white); color: #4a5560; font-size: 6.2px; line-height: 7.4px;
    display: flex; flex-direction: column; align-items: center; justify-content: center;
    text-align: center; transform: rotate(9deg); padding: 0 6px; }
  .help-sticker .mail { color: var(--ink-olive); font-weight: 600; }

  .origin-badge { left: 795px; top: 627px; }

  .content-box { left: 341px; top: 773px; width: 520px; height: 66px; border: 2.5px solid var(--ink-white);
    border-radius: 16px; text-align: center; padding-top: 9px; }
  .content-box .lead { font-size: 16px; font-weight: 700; line-height: 20px; }
  .content-box .detail { font-size: 16px; font-weight: 400; line-height: 22px; }

  .content-en { top: 858px; color: var(--ink-muted); font-size: 14px; line-height: 19px; }
  .content-en .lead { font-weight: 700; }

  .measure-label { color: var(--measure); font-size: 19px; }
  .measure-label--h120 { left: 98px; top: 748px; transform: rotate(90deg); transform-origin: left top; left: 126px; top: 728px; }
  .measure-label--h45 { left: 126px; top: 965px; transform: rotate(90deg); transform-origin: left top; }
  .measure-label--w215 { top: 1091px; }
</style>
</head>
<body>
<main class="dieline-sheet">
  <svg class="lines" width="1200" height="1109" viewBox="0 0 1200 1109" aria-hidden="true">
    <g fill="none" stroke="var(--panel-edge)" stroke-width="1">
      <line x1="177" y1="0" x2="177" y2="591"/>
      <line x1="1023" y1="0" x2="1023" y2="591"/>
      <line x1="297" y1="0" x2="297" y2="1109"/>
      <line x1="902" y1="0" x2="902" y2="1109"/>
      <line x1="297" y1="127" x2="902" y2="127"/>
      <line x1="297" y1="465" x2="902" y2="465"/>
      <line x1="177" y1="591" x2="1023" y2="591"/>
      <rect x="308" y="573" width="605" height="337"/>
      <line x1="297" y1="929" x2="902" y2="929"/>
      <line x1="297" y1="1056" x2="902" y2="1056"/>
    </g>
    <g fill="none" stroke="var(--fold)" stroke-width="1">
      <line x1="159" y1="127" x2="159" y2="465"/>
      <line x1="171" y1="127" x2="171" y2="465"/>
      <line x1="297" y1="127" x2="297" y2="465"/>
      <line x1="902" y1="127" x2="902" y2="465"/>
      <line x1="1029" y1="127" x2="1029" y2="465"/>
      <line x1="1041" y1="127" x2="1041" y2="465"/>
    </g>
    <g fill="none" stroke="var(--die-cut)" stroke-width="1.1">
      <path d="M159 127 L156 132 L42 132 L42 246 L33 250 L33 341 L42 345 L42 459 L156 459 L159 465"/>
      <path d="M1041 127 L1044 132 L1157 132 L1157 246 L1167 250 L1167 341 L1157 345 L1157 459 L1044 459 L1041 465"/>
      <path d="M159 127 L297 127 M159 465 L297 465 M902 127 L1041 127 M902 465 L1041 465"/>
      <path d="M298 246 L308 246 L308 345 L298 345"/>
      <path d="M901 246 L891 246 L891 345 L901 345"/>
      <path d="M297 591 L189 651 C172 662 165 680 165 700 L165 810 C165 830 174 852 189 867 L297 929"/>
      <path d="M902 591 L1011 651 C1028 662 1035 680 1035 700 L1035 810 C1035 830 1026 852 1011 867 L902 929"/>
      <path d="M297 929 L213 933 C192 936 185 952 190 972 C205 1018 245 1052 297 1056"/>
      <path d="M902 929 L987 933 C1008 936 1015 952 1010 972 C995 1018 955 1052 902 1056"/>
    </g>
    <g stroke="var(--measure)" stroke-width="1" fill="var(--measure)">
      <line x1="115" y1="593" x2="115" y2="927"/>
      <line x1="115" y1="931" x2="115" y2="1054"/>
      <line x1="108" y1="929" x2="297" y2="929" stroke-opacity=".6"/>
      <line x1="108" y1="1056" x2="297" y2="1056" stroke-opacity=".6"/>
      <line x1="299" y1="1102" x2="900" y2="1102"/>
      <path d="M115 593 l-3 8 h6z M115 927 l-3 -8 h6z M115 931 l-3 8 h6z M115 1054 l-3 -8 h6z M299 1102 l9 -3 v6z M900 1102 l-9 -3 v6z" stroke="none"/>
    </g>
  </svg>

  <p class="abs center-x thanks">Vielen Dank für dein Vertrauen in NESTORA.</p>

  <ul class="abs features features--de">
    <li><svg viewBox="0 0 14 14"><rect x="1.5" y="1.5" width="11" height="11" rx="2" fill="none" stroke="#9aa3ab"/></svg>UNSICHTBARER SCHUTZ</li>
    <li><svg viewBox="0 0 14 14"><path d="M11 3 A5 5 0 1 0 11 11" fill="none" stroke="#9aa3ab" stroke-width="1.3"/></svg>LEISTUNGSSTARKE MAGNETSCHLÜSSEL</li>
    <li><svg viewBox="0 0 14 14"><path d="M2 12 L4 8 L10 2 L12 4 L6 10 Z" fill="none" stroke="#9aa3ab"/></svg>HOHE KLEBEWIRKUNG</li>
    <li><svg viewBox="0 0 14 14"><circle cx="7" cy="7" r="5.5" fill="none" stroke="#9aa3ab"/><path d="M4.5 7 L6.3 8.8 L9.5 5.3" fill="none" stroke="#9aa3ab"/></svg>FRUSTFREIES MONTAGE-SET</li>
  </ul>
  <ul class="abs features features--en">
    <li><svg viewBox="0 0 14 14"><rect x="1.5" y="1.5" width="11" height="11" rx="2" fill="none" stroke="#8a949d"/></svg>INVISIBLE PROTECTION</li>
    <li><svg viewBox="0 0 14 14"><path d="M11 3 A5 5 0 1 0 11 11" fill="none" stroke="#8a949d" stroke-width="1.3"/></svg>HIGH-STRENGTH MAGNETIC KEY</li>
    <li><svg viewBox="0 0 14 14"><path d="M2 12 L4 8 L10 2 L12 4 L6 10 Z" fill="none" stroke="#8a949d"/></svg>HIGH-PERFORMANCE ADHESION</li>
    <li><svg viewBox="0 0 14 14"><circle cx="7" cy="7" r="5.5" fill="none" stroke="#8a949d"/><path d="M4.5 7 L6.3 8.8 L9.5 5.3" fill="none" stroke="#8a949d"/></svg>HASSLE-FREE INSTALLATION KIT</li>
  </ul>

  <div class="abs warning warning--de">
    <p>ACHTUNG: Dies ist kein Spielzeug. Anbringung gemäß<br>der beiliegenden Montageanleitung durchführen.<br>Regelmäßig festen Sitz prüfen.<br>24 Stunden nach Montage nicht belasten.</p>
    <p>Bei Fragen helfen wir gerne weiter: hallo@nestora-beispiel.de</p>
  </div>
  <div class="abs warning warning--en">
    <p>WARNING: This is not a toy. Install according to the<br>enclosed installation instructions.<br>Check regularly to ensure secure attachment.<br>Do not apply load for 24 hours after installation.</p>
    <p>For any questions we will be happy to assist you:<br>hallo@nestora-beispiel.de</p>
  </div>

  <div class="abs imprint">
    <span>NESTORA Kindersicherung Schrank 12 Stk.</span><br>
    <span>Lena Brandt</span><br>
    <span>Lindenweg 12</span><br>
    <span>70000 Musterstadt - Germany</span><br>
    <span class="gap">Art.Nr.: xxxxx</span><br>
    <span>Made in PCR</span><br>
    <span>Batch Number: xxxx</span>
  </div>

  <p class="abs center-x wordmark wordmark--lid">nestora</p>
  <p class="abs center-x tagline tagline--lid">Thoughtfully designed - for a relaxed home.</p>

  <div class="abs help-sticker">
    <p>If you have any<br>questions or suggestions,<br>we're always happy to help:</p>
    <p class="mail">hallo@nestora-beispiel.de</p>
  </div>

  <p class="abs center-x wordmark wordmark--front">nestora</p>
  <svg class="abs origin-badge" width="66" height="66" viewBox="0 0 66 66" role="img" aria-label="Herkunftssiegel">
    <circle cx="33" cy="33" r="32" fill="#ffffff"/>
    <circle cx="33" cy="33" r="22" fill="var(--board)"/>
  </svg>
  <p class="abs center-x tagline tagline--front">Damit neugierige Babys sicher die Welt entdecken können.</p>

  <div class="abs content-box">
    <p class="lead">12 unsichtbare Kindersicherungen für Schränke und Schubladen</p>
    <p class="detail">10 Magnetschlösser mit 2 Schlüsseln · 2 Quick-Locks</p>
  </div>
  <div class="abs center-x content-en">
    <p class="lead">12 invisible safety cupboard lock</p>
    <p>10 magnetic locks with 2 key · 2 Quick-Locks</p>
  </div>

  <p class="abs center-x wordmark wordmark--base">nestora</p>
  <p class="abs center-x tagline tagline--base">Mit Sorgfalt enwickelt. Für ein entspanntes Zuhause.</p>

  <p class="abs measure-label measure-label--h120">120 mm</p>
  <p class="abs measure-label measure-label--h45">45 mm</p>
  <p class="abs center-x measure-label measure-label--w215">215 mm</p>
</main>
</body>
</html>
```